Industry/Entity Type

Business

Contact Information for Business Card

Dario Kelvern - Managing Director

T: 1300 682 905
E: dario@bkdatasolutions.com.au
W: bkdatasolutions.com.au

PO BOX 7
HALDEN RIDGE VIC 3362

```html
<!DOCTYPE html>
<html lang="en">
<head>
<meta charset="utf-8">
<title>BK Data Solutions — Business Card</title>
<link rel="stylesheet" href="https://fonts.googleapis.com/css2?family=Lato:wght@400;700;900&display=swap">
<style>
  :root {
    --stage: #3a3a3a;
    --navy: #283891;
    --sky: #1ba9e8;
    --paper: #ffffff;
    --ink: #1c1c1c;
  }
  * { box-sizing: border-box; margin: 0; padding: 0; }
  html, body { width: 1200px; height: 900px; overflow: hidden; }
  body {
    background: var(--stage);
    font-family: "Lato", Arial, sans-serif;
    position: relative;
  }
  .card {
    position: absolute;
    left: 285px;
    width: 630px;
    height: 360px;
    overflow: hidden;
  }
  .card--back { top: 60px; background: var(--navy); }
  .card--front { top: 480px; background: var(--paper); }

  .brand {
    display: flex;
    align-items: center;
    gap: 12px;
    font-weight: 900;
    line-height: 1;
    letter-spacing: -0.5px;
  }
  .brand__mark { display: block; flex: none; }

  .card--back .brand {
    position: absolute;
    left: 0; right: 0; top: 120px;
    justify-content: center;
    color: var(--paper);
    font-size: 50px;
  }
  .card--back .brand__mark { width: 38px; height: 38px; background: var(--sky); }
  .card--back .web {
    position: absolute;
    left: 0; right: 0; top: 232px;
    text-align: center;
    color: var(--paper);
    font-size: 17px;
    letter-spacing: 0.3px;
  }

  .card--front .brand {
    position: absolute;
    left: 60px; top: 44px;
    color: var(--navy);
    font-size: 40px;
  }
  .card--front .brand__mark { width: 30px; height: 30px; background: var(--sky); }

  .contact {
    position: absolute;
    left: 50px; top: 130px;
    color: var(--ink);
    font-size: 16px;
    line-height: 1.35;
  }
  .contact__address { padding-left: 24px; margin-bottom: 6px; }
  .contact__line { display: flex; align-items: center; gap: 8px; }
  .contact__icon { width: 16px; height: 16px; flex: none; }

  .band { position: absolute; left: 0; top: 0; width: 630px; height: 360px; }

  .person {
    position: absolute;
    right: 60px; top: 226px;
    text-align: left;
  }
  .person__name { color: var(--sky); font-size: 24px; font-weight: 700; line-height: 1.15; }
  .person__role { color: var(--ink); font-size: 16px; margin-top: 2px; }

  .card--front .web {
    position: absolute;
    right: 120px; bottom: 16px;
    color: var(--paper);
    font-size: 17px;
    letter-spacing: 0.3px;
  }
</style>
</head>
<body>

<section class="card card--back" aria-label="Business card, back">
  <div class="brand"><span class="brand__mark"></span><span class="brand__name">BK Data Solutions</span></div>
  <p class="web">www.bkdatasolutions.com.au</p>
</section>

<section class="card card--front" aria-label="Business card, front">
  <svg class="band" viewBox="0 0 630 360" aria-hidden="true">
    <path d="M0 270 C 180 290, 380 320, 630 312 L630 360 L0 360 Z" fill="var(--navy)"/>
    <path d="M0 262 C 200 276, 400 300, 630 300 L630 316 C 400 320, 200 290, 0 270 Z" fill="var(--sky)"/>
    <path d="M0 270 C 200 290, 400 320, 630 316 L630 322 C 400 326, 200 296, 0 276 Z" fill="var(--paper)"/>
  </svg>

  <div class="brand"><span class="brand__mark"></span><span class="brand__name">BK Data Solutions</span></div>

  <div class="contact">
    <p class="contact__address">PO Box 7<br>Halden Ridge Vic 3362</p>
    <p class="contact__line">
      <svg class="contact__icon" viewBox="0 0 16 16" aria-hidden="true"><path d="M4 1.5l2.2 3-1.4 1.6c.8 1.8 2.2 3.3 4.1 4.2l1.6-1.4 3 2.2-1.2 2.6C7 13.4 2.6 9 1.7 2.7z" fill="var(--sky)"/></svg>
      <span>1300 682 905</span>
    </p>
    <p class="contact__line">
      <svg class="contact__icon" viewBox="0 0 16 16" aria-hidden="true"><rect x="1" y="3.5" width="14" height="9.5" fill="var(--sky)"/><path d="M1.5 4l6.5 5 6.5-5" fill="none" stroke="#fff" stroke-width="1.2"/></svg>
      <span>dario@bkdatasolutions.com.au</span>
    </p>
  </div>

  <div class="person">
    <p class="person__name">Dario Kelvern</p>
    <p class="person__role">Managing Director</p>
  </div>

  <p class="web">www.bkdatasolutions.com.au</p>
</section>

</body>
</html>
```